Kestrel Roofing & Restoration Business Card Design

Lookiing for a double sided business card design that will have rounded corners, will look good with Spot UV, Soft Laminate, or Gloss
Front of card should have Logo, Name and Contact Info, License numbers
Back of card should have Logo, maybe other small details

```html
<!DOCTYPE html>
<html lang="en">
<head>
<meta charset="utf-8">
<title>Kestrel Roofing &amp; Restoration – Business Card</title>
<link href="https://fonts.googleapis.com/css2?family=Poppins:wght@400;500;600;700&display=swap" rel="stylesheet">
<style>
  :root {
    --stage: #2a2a2a;
    --card: #232324;
    --card-edge: #1b1b1c;
    --accent: #11a3e6;
    --ink: #ffffff;
    --muted: #cfd3d6;
    --emboss: #3a3a3c;
  }
  * { margin: 0; padding: 0; box-sizing: border-box; }
  html, body { width: 1200px; height: 875px; overflow: hidden; }
  body {
    background: var(--stage);
    font-family: "Poppins", sans-serif;
    position: relative;
  }
  .card {
    position: absolute;
    width: 560px;
    height: 320px;
    background: var(--card);
    border-radius: 24px;
    box-shadow: 0 18px 40px rgba(0,0,0,.45);
    overflow: hidden;
  }
  /* Back side */
  .card--back {
    left: 70px; top: 80px;
    border-right: 3px solid var(--accent);
    border-bottom: 3px solid var(--accent);
  }
  .back-mark {
    position: absolute;
    left: 40px; top: 50px;
    font-size: 118px;
    font-weight: 700;
    letter-spacing: -2px;
    color: var(--emboss);
    line-height: 1;
  }
  .back-lockup {
    position: absolute;
    right: 40px; bottom: 34px;
  }
  /* Front side */
  .card--front {
    left: 570px; top: 470px;
    border-left: 3px solid var(--accent);
    border-bottom: 3px solid var(--accent);
  }
  .front-tab {
    position: absolute;
    left: 0; top: 150px;
    width: 8px; height: 22px;
    background: var(--accent);
  }
  .front-lockup {
    position: absolute;
    left: 44px; top: 38px;
  }
  /* Shared lockup */
  .lockup { display: flex; align-items: center; gap: 12px; }
  .lockup-name {
    font-size: 30px;
    font-weight: 700;
    color: var(--ink);
    line-height: 1;
  }
  .lockup-divider {
    width: 2px; height: 44px;
    background: var(--accent);
  }
  .lockup-tagline {
    font-size: 17px;
    font-weight: 500;
    color: var(--ink);
    line-height: 1.15;
    letter-spacing: .5px;
  }
  .holder {
    position: absolute;
    left: 44px; top: 130px;
  }
  .holder-name {
    font-size: 24px;
    font-weight: 600;
    color: var(--accent);
    line-height: 1.1;
  }
  .holder-role {
    font-size: 13px;
    color: var(--ink);
    margin-top: 2px;
  }
  .holder-license {
    font-size: 13px;
    color: var(--ink);
    margin-top: 6px;
  }
  .holder-license span { color: var(--accent); }
  .contact-list {
    position: absolute;
    left: 44px; top: 222px;
    list-style: none;
  }
  .contact-list li {
    display: flex; align-items: center; gap: 8px;
    font-size: 12.5px;
    color: var(--ink);
    line-height: 19px;
  }
  .contact-list svg { width: 11px; height: 11px; fill: var(--accent); }
  .address {
    position: absolute;
    right: 40px; top: 150px;
    display: flex; align-items: center; gap: 10px;
    font-size: 12px;
    color: var(--ink);
    line-height: 1.35;
  }
  .address-divider { width: 2px; height: 30px; background: var(--accent); }
</style>
</head>
<body>

<section class="card card--back" aria-label="Business card back">
  <div class="back-mark">Kestrel</div>
  <div class="lockup back-lockup">
    <span class="lockup-name">Kestrel</span>
    <span class="lockup-divider"></span>
    <span class="lockup-tagline">ROOFING &amp;<br>RESTORATION</span>
  </div>
</section>

<section class="card card--front" aria-label="Business card front">
  <span class="front-tab"></span>
  <div class="lockup front-lockup">
    <span class="lockup-name">Kestrel</span>
    <span class="lockup-divider"></span>
    <span class="lockup-tagline">ROOFING &amp;<br>RESTORATION</span>
  </div>

  <div class="holder">
    <p class="holder-name">Daniel Harper</p>
    <p class="holder-role">Head contractor</p>
    <p class="holder-license"><span>License</span> #40817</p>
  </div>

  <ul class="contact-list">
    <li><svg viewBox="0 0 24 24"><path d="M6.6 10.8a15 15 0 0 0 6.6 6.6l2.2-2.2a1 1 0 0 1 1-.25 11.4 11.4 0 0 0 3.6.57 1 1 0 0 1 1 1V20a1 1 0 0 1-1 1A17 17 0 0 1 3 4a1 1 0 0 1 1-1h3.5a1 1 0 0 1 1 1c0 1.25.2 2.45.57 3.57a1 1 0 0 1-.25 1z"/></svg>+44 7700 900418</li>
    <li><svg viewBox="0 0 24 24"><path d="M7 1h10a2 2 0 0 1 2 2v18a2 2 0 0 1-2 2H7a2 2 0 0 1-2-2V3a2 2 0 0 1 2-2zm0 3v14h10V4z"/></svg>+44 7700 900418</li>
    <li><svg viewBox="0 0 24 24"><path d="M2 5h20v14H2zm2 2v.5l8 5 8-5V7l-8 5z"/></svg>name@kestrelroofing.co.uk</li>
    <li><svg viewBox="0 0 24 24"><circle cx="12" cy="12" r="10"/></svg>www.kestrelroofing.co.uk</li>
  </ul>

  <div class="address">
    <span class="address-divider"></span>
    <p>48 Harbour Lane<br>Ashford, NJ 07012 USA</p>
  </div>
</section>

</body>
</html>
```